New website for a commercial real estate consulting company

What we’re looking for in a new web site:
• Desktop and mobile friendly
• Clear navigation
• Strong graphics
• Professional appearance
• The ability to update it ourselves
• Site is for information purposes only – no transactions required
• Traffic counts – number of visits per page?
• A firm quote on costs to develop and launch
• SSL
Attached is a copy of the revised text we propose to use, including our new logo. (The pagination can be different than as shown.)
Our current website address is www.tamblinvaleadvisory.ca

```html
<!DOCTYPE html>
<html lang="en">
<head>
<meta charset="utf-8">
<title>Tamblin Vale Advisory</title>
<link href="https://fonts.googleapis.com/css2?family=Cinzel:wght@400;600&family=Lato:ital,wght@0,400;0,700;1,400;1,700&family=Open+Sans:ital,wght@1,600&display=swap" rel="stylesheet">
<style>
:root{
  --navy:#262d8c;
  --ink:#222;
  --body:#444;
  --muted:#666;
  --grey-bg:#f3f3f3;
  --line:#cfcfcf;
  --white:#fff;
}
*{box-sizing:border-box;margin:0;padding:0}
html,body{width:1200px;height:4534px;overflow:hidden}
body{position:relative;background:var(--white);font-family:"Lato",sans-serif;color:var(--body)}
.abs{position:absolute}
.heading{font-family:"Cinzel",serif;font-weight:400;color:var(--ink);letter-spacing:2px;text-align:center;font-size:33px}
.rule{width:84px;height:3px;background:var(--navy);margin:16px auto 0}
.btn{display:inline-block;background:var(--navy);color:#fff;font-family:"Cinzel",serif;font-size:16px;letter-spacing:1px;padding:15px 34px;border-radius:30px}
.btn-ghost{display:inline-block;border:1px solid #bbb;color:#333;font-family:"Cinzel",serif;font-size:13px;padding:10px 26px;border-radius:24px;background:#fff}

/* header */
.site-header{top:0;left:0;width:1200px;height:115px;background:#fff}
.nav{position:absolute;right:72px;top:44px;display:flex;gap:34px;font-family:"Cinzel",serif;font-size:14px;color:#333}
.nav .active{color:var(--navy)}
.brand{top:-60px;left:100px;width:300px;height:300px;border-radius:50%;background:#fff;z-index:3;display:flex;align-items:flex-end;justify-content:center;padding-bottom:62px}
.brand span{font-family:"Cinzel",serif;color:var(--navy);font-size:20px;font-weight:600;text-align:center;line-height:1.25;width:170px}

/* hero */
.hero{top:115px;left:0;width:1200px;height:545px;background:linear-gradient(160deg,#9fc3ea 0%,#3f77c4 45%,#1d3f86 100%)}
.hero h1{position:absolute;top:178px;width:100%;text-align:center;font-family:"Cinzel",serif;font-weight:400;color:#fff;font-size:66px;line-height:88px;letter-spacing:2px}
.hero .arrow{position:absolute;top:250px}

/* welcome */
.welcome{top:720px;left:80px;width:1040px;text-align:center}
.welcome p{font-size:15.5px;line-height:29px;margin-top:38px;color:#333}
.welcome blockquote{margin-top:30px;font-style:italic;color:var(--navy);font-size:17px;line-height:30px}

/* who */
.who-title{top:1098px;left:0;width:1200px}
.portrait{top:1208px;left:106px;width:356px;height:534px;border:8px solid #fff;box-shadow:0 0 0 1px #ddd;background:linear-gradient(180deg,#c8a27a 0%,#b9473f 55%,#c9272f 100%)}
.bio{top:1222px;left:508px;width:490px}
.bio h3{font-family:"Cinzel",serif;font-weight:400;font-size:27px;color:#333}
.bio .mail{color:var(--navy);font-style:italic;font-size:13px;margin-top:14px}
.bio p{font-size:12.5px;line-height:24px;margin-top:16px;color:#555}
.bio ul{list-style:none;margin-top:22px}
.bio li{display:flex;gap:14px;font-size:12.5px;line-height:23px;margin-bottom:14px;color:#555}
.bio li svg{flex:none;margin-top:6px}
.bio .btn{margin-top:10px}

/* what we do */
.services{top:1833px;left:0;width:1200px;height:1262px;background:var(--grey-bg)}
.services .heading{margin-top:60px}
.timeline{position:absolute;left:600px;top:170px;width:1px;height:1060px;background:var(--line)}
.dot{position:absolute;left:593px;width:15px;height:15px;border-radius:50%;border:1px solid #aaa;background:var(--grey-bg)}
.dot::after{content:"";position:absolute;left:4px;top:4px;width:5px;height:5px;border-radius:50%;background:#888}
.svc-img{position:absolute;width:454px;height:205px}
.svc-text{position:absolute;width:440px;font-size:12.5px;line-height:23px;color:#555}
.svc-text h4{font-family:"Lato",sans-serif;font-weight:400;font-size:19px;color:#333;margin-bottom:18px}
.svc-text.right-al{text-align:right}
.svc-text .btn-ghost{margin-top:14px}

/* clients */
.clients{top:3095px;left:0;width:1200px;height:499px}
.clients h2{position:absolute;left:76px;top:64px;font-family:"Cinzel",serif;font-weight:400;font-size:33px;color:var(--ink)}
.client-list{position:absolute;left:76px;top:176px;display:grid;grid-template-columns:240px 240px;row-gap:20px;font-size:15px;color:#444}
.client-list div{display:flex;gap:12px;line-height:20px}
.clients-photo{position:absolute;right:0;top:0;width:602px;height:499px;background:linear-gradient(135deg,#e7dccd 0%,#b07a55 50%,#5a3b2a 100%)}

.quote-band{top:3594px;left:0;width:1200px;height:118px;background:var(--navy);color:#fff;text-align:center;font-family:"Open Sans",sans-serif;font-style:italic;font-weight:600;font-size:28px;line-height:118px}

/* events */
.events-title{top:3755px;left:0;width:1200px}
.events{top:3865px;left:88px;width:1024px;display:flex;justify-content:space-between}
.event{width:300px}
.event .tag{display:inline-block;border:1px solid #aaa;border-radius:20px;padding:7px 20px;font-family:"Cinzel",serif;font-size:14px;color:#333}
.event h5{font-family:"Cinzel",serif;font-weight:400;color:var(--navy);font-size:18px;margin-top:14px}
.event p{font-size:14px;line-height:20px;margin-top:10px;color:#333}
.event .more{font-family:"Cinzel",serif;font-size:13px;color:var(--navy);margin-top:12px}
.ev-arrow{top:3950px}
.events-btn{top:4110px;left:0;width:1200px;text-align:center}

/* footer */
.site-footer{top:4213px;left:0;width:1200px;height:321px;background:var(--grey-bg)}
.foot-brand{position:absolute;left:76px;top:80px;font-family:"Cinzel",serif;font-weight:600;color:var(--navy);font-size:19px;line-height:24px;width:180px;text-align:center}
.copy{position:absolute;left:76px;top:206px;font-size:12px;color:#333}
.foot-col{position:absolute;top:50px}
.foot-col h6{font-family:"Cinzel",serif;font-weight:400;color:var(--navy);font-size:18px;margin-bottom:18px}
.foot-col ul{list-style:none;font-size:11.5px;line-height:27px;color:#333}
.contact-row{display:flex;gap:10px;font-size:12px;line-height:17px;color:#333;margin-bottom:18px}
.people{position:absolute;left:864px;top:95px;font-size:12px;line-height:17px;color:#333}
.people div{margin-bottom:20px}
</style>
</head>
<body>

<header class="abs site-header">
  <nav class="nav">
    <span class="active">Home</span><span>Who We Are</span><span>What We Do</span><span>Our Clients</span><span>Contact Us</span><span>Industry Events Calendar</span>
  </nav>
</header>
<div class="abs brand"><span>Tamblin Vale Advisory</span></div>

<section class="abs hero" role="img" aria-label="Photo looking up at glass office towers against a blue sky">
  <h1>Expert. Professional.<br>Cost Effective</h1>
  <svg class="arrow" style="left:86px" width="24" height="40" viewBox="0 0 24 40"><path d="M20 4 4 20l16 16" fill="none" stroke="#fff" stroke-width="3"/></svg>
  <svg class="arrow" style="right:86px" width="24" height="40" viewBox="0 0 24 40"><path d="M4 4l16 16L4 36" fill="none" stroke="#fff" stroke-width="3"/></svg>
</section>

<section class="abs welcome">
  <h2 class="heading">Welcome to Tamblin Vale Advisory</h2>
  <p>Tamblin Vale Advisory is an independent consulting firm offering practical, hands-on assistance to the commercial real estate and commercial mortgage lending industries. We specialize in financial analysis, underwriting and financial due diligence.<br>Working with us, you get top notch help when you need it – and only when you need it – one project at a time. Tamblin Vale Advisory has been providing expert, professional and cost-effective service to the commercial real estate and commercial mortgage industries since 2001. We have worked on projects across Canada and the United States, and in every major property type.</p>
  <blockquote>"The foundation of our success has been our commitment to exceeding our clients expectations, both in quality and in timeliness. We strive to go above and beyond on every assignment."</blockquote>
</section>

<div class="abs who-title"><h2 class="heading">Who We Are</h2><div class="rule"></div></div>
<div class="abs portrait" role="img" aria-label="Portrait photo of Helen Brackley"></div>
<section class="abs bio">
  <h3>Helen Brackley, MBA, MRICS</h3>
  <div class="mail">helen.brackley@tamblinvaleadvisory.ca</div>
  <p>Helen has more than 30 years' senior experience in a wide range of property types. Her expertise encompasses all aspects of the financing, valuation, purchase and sale of commercial real estate. Prior to founding Tamblin Vale Advisory in 2001, Helen spent 16 years of her career in a variety of institutional roles, culminating in ten years as Vice-President, Property Investments of a company. Working in a leadership capacity, Helen's career also includes:</p>
  <ul>
    <li><svg width="12" height="10" viewBox="0 0 12 10"><path d="M1 5l3.5 3.5L11 1" fill="none" stroke="#262d8c" stroke-width="2"/></svg>Acquisitions, dispositions, and asset management for a life company's equity real estate portfolio.</li>
    <li><svg width="12" height="10" viewBox="0 0 12 10"><path d="M1 5l3.5 3.5L11 1" fill="none" stroke="#262d8c" stroke-width="2"/></svg>Roles on both the buy and the sell sides of a corporate sale - on the due diligence team for two life insurance companies; key member of the selling team for a life insurance company.</li>
    <li><svg width="12" height="10" viewBox="0 0 12 10"><path d="M1 5l3.5 3.5L11 1" fill="none" stroke="#262d8c" stroke-width="2"/></svg>Corporate secretary of a life insurance company for five years.</li>
  </ul>
  <span class="btn">Read More</span>
</section>

<section class="abs services">
  <h2 class="heading">What We Do</h2><div class="rule"></div>
  <div class="timeline"></div>
  <div class="dot" style="top:250px"></div>
  <div class="dot" style="top:525px"></div>
  <div class="dot" style="top:800px"></div>
  <div class="dot" style="top:1080px"></div>

  <div class="svc-text right-al" style="left:122px;top:170px"><h4>FOR OWNERS</h4>With sixty years of varied and progressive industry experience, we have the expertise to quickly grasp the priorities and challenges of your organization sixty years of varied and progressive industry experience<br><span class="btn-ghost">Read More</span></div>
  <div class="svc-img" style="left:643px;top:163px;background:linear-gradient(180deg,#8fb3d6,#c98a3c)" role="img" aria-label="Photo of construction cranes over a building site"></div>

  <div class="svc-img" style="left:112px;top:438px;background:linear-gradient(135deg,#e0b060,#8a4a1a)" role="img" aria-label="Photo of eyeglasses resting on financial papers"></div>
  <div class="svc-text" style="left:650px;top:445px"><h4>FOR BUYERS</h4>Our people have participated in transactions from all sides: as vendor, as lender and as advisor, on deals of $1 million to more than $100 what each side needs and wants to know about a property<br><span class="btn-ghost">Read More</span></div>

  <div class="svc-text right-al" style="left:122px;top:717px"><h4>FOR LENDERS</h4>Today's real estate lenders are squeezed between the triple pressures of aggressive lending targets, staff budget constraints and ever-tightening regulation. Everyone is being asked to "do more, with less<br><span class="btn-ghost">Read More</span></div>
  <div class="svc-img" style="left:643px;top:710px;background:linear-gradient(135deg,#d9d4cc,#5b4a3c)" role="img" aria-label="Photo of a desk with laptop, documents and coffee"></div>

  <div class="svc-img" style="left:112px;top:985px;background:linear-gradient(135deg,#eef2f6,#7f8fa3)" role="img" aria-label="Photo of a business handshake over a desk"></div>
  <div class="svc-text" style="left:650px;top:990px"><h4>FOR BROKERS</h4>Our people have participated in transactions from all sides: as buyer, as vendor, as lender and as advisor, on deals of $1 million to more than $100 million.We know from personal wants to know about a property.<br><span class="btn-ghost">Read More</span></div>
</section>

<section class="abs clients">
  <h2>Our Clients :</h2>
  <div class="client-list">
    <div><svg width="16" height="16" viewBox="0 0 16 16"><circle cx="8" cy="8" r="8" fill="#262d8c"/><path d="M4.5 8.2l2.3 2.3 4.7-4.7" fill="none" stroke="#fff" stroke-width="1.8"/></svg>Chartered banks</div>
    <div><svg width="16" height="16" viewBox="0 0 16 16"><circle cx="8" cy="8" r="8" fill="#262d8c"/><path d="M4.5 8.2l2.3 2.3 4.7-4.7" fill="none" stroke="#fff" stroke-width="1.8"/></svg>Life insurance companies</div>
    <div><svg width="16" height="16" viewBox="0 0 16 16"><circle cx="8" cy="8" r="8" fill="#262d8c"/><path d="M4.5 8.2l2.3 2.3 4.7-4.7" fill="none" stroke="#fff" stroke-width="1.8"/></svg>Mortgage bankers</div>
    <div><svg width="16" height="16" viewBox="0 0 16 16"><circle cx="8" cy="8" r="8" fill="#262d8c"/><path d="M4.5 8.2l2.3 2.3 4.7-4.7" fill="none" stroke="#fff" stroke-width="1.8"/></svg>Pension funds</div>
    <div><svg width="16" height="16" viewBox="0 0 16 16"><circle cx="8" cy="8" r="8" fill="#262d8c"/><path d="M4.5 8.2l2.3 2.3 4.7-4.7" fill="none" stroke="#fff" stroke-width="1.8"/></svg>Public REITs &amp; REOCs</div>
    <div><svg width="16" height="16" viewBox="0 0 16 16"><circle cx="8" cy="8" r="8" fill="#262d8c"/><path d="M4.5 8.2l2.3 2.3 4.7-4.7" fill="none" stroke="#fff" stroke-width="1.8"/></svg>Non-bank lenders</div>
    <div><svg width="16" height="16" viewBox="0 0 16 16"><circle cx="8" cy="8" r="8" fill="#262d8c"/><path d="M4.5 8.2l2.3 2.3 4.7-4.7" fill="none" stroke="#fff" stroke-width="1.8"/></svg>Private equity firms</div>
    <div><svg width="16" height="16" viewBox="0 0 16 16"><circle cx="8" cy="8" r="8" fill="#262d8c"/><path d="M4.5 8.2l2.3 2.3 4.7-4.7" fill="none" stroke="#fff" stroke-width="1.8"/></svg>Brokerage firms</div>
    <div><svg width="16" height="16" viewBox="0 0 16 16" style="flex:none"><circle cx="8" cy="8" r="8" fill="#262d8c"/><path d="M4.5 8.2l2.3 2.3 4.7-4.7" fill="none" stroke="#fff" stroke-width="1.8"/></svg>Family-owned real estate investment companies</div>
  </div>
  <div class="clients-photo" role="img" aria-label="Photo of many raised hands meeting in a team high five"></div>
</section>

<div class="abs quote-band">“Reputation is the currency of the 21 st century”</div>

<div class="abs events-title"><h2 class="heading">Industry Events Calendar</h2><div class="rule"></div></div>
<svg class="abs ev-arrow" style="left:40px" width="20" height="34" viewBox="0 0 20 34"><path d="M17 3 3 17l14 14" fill="none" stroke="#444" stroke-width="3"/></svg>
<svg class="abs ev-arrow" style="right:40px" width="20" height="34" viewBox="0 0 20 34"><path d="M3 3l14 14L3 31" fill="none" stroke="#444" stroke-width="3"/></svg>
<section class="abs events">
  <article class="event"><span class="tag">January 2019</span><h5>27-29 Pacific Retail Forum</h5><p>Fusce finibus nunc diam, ut efficitur massa interdum interdum. Nulla ullamcorper mattis dui a rhoncus.</p><div class="more">Read More</div></article>
  <article class="event"><span class="tag">February 2019</span><h5>26 Capital Exchange</h5><p>Fusce finibus nunc diam, ut efficitur massa interdum interdum. Nulla ullamcorper mattis dui a rhoncus.</p><div class="more">Read More</div></article>
  <article class="event"><span class="tag">March 2019</span><h5>6 Toronto Property Council AGM</h5><p>Fusce finibus nunc diam, ut efficitur massa interdum interdum. Nulla ullamcorper mattis dui a rhoncus.</p><div class="more">Read More</div></article>
</section>
<div class="abs events-btn"><span class="btn">View All Events</span></div>

<footer class="abs site-footer">
  <div class="foot-brand">Tamblin Vale Advisory</div>
  <div class="copy">© 2019. Tamblin Vale Advisory.</div>
  <div class="foot-col" style="left:340px">
    <h6>Quick Links</h6>
    <ul><li>Home</li><li>Who We Are</li><li>What We Do</li><li>Our Clients</li><li>Contact Us</li><li>Industry Events Calendar</li></ul>
  </div>
  <div class="foot-col" style="left:582px">
    <h6>Contact Us</h6>
    <div class="contact-row"><svg width="12" height="16" viewBox="0 0 12 16"><path d="M6 0a6 6 0 0 0-6 6c0 4.5 6 10 6 10s6-5.5 6-10a6 6 0 0 0-6-6zm0 8.5A2.5 2.5 0 1 1 6 3.5a2.5 2.5 0 0 1 0 5z" fill="#262d8c"/></svg><span>Tamblin Vale Advisory<br>48 Larchmont Road<br>Milbrook, Ontario L0B 2X4</span></div>
    <div class="contact-row"><svg width="14" height="14" viewBox="0 0 14 14"><rect x="2" y="5" width="10" height="7" fill="#262d8c"/><rect x="4" y="1" width="6" height="4" fill="none" stroke="#262d8c" stroke-width="1.5"/></svg><span>Fax: 905-555-0190</span></div>
  </div>
  <div class="people">
    <div>Helen Brackley<br>905-555-0142<br>helen.brackley@tamblinvaleadvisory.ca</div>
    <div>Daniel Orsk<br>905-555-0176<br>daniel.orsk@tamblinvaleadvisory.ca</div>
  </div>
</footer>

</body>
</html>
```